International sports trophy business needs a web design

We need two pages designed for a new company called medalnook. We sell innovative sports trophies via our website and store details of past purchases to allow returning customers to easily place their orders. Customers can log into their accounts using palsora or a secondary account login button. The final design should be clean and should focus on the theme of winning the trophy as it is applicable to all sports.

The page should be designed with themes that can be used throughout the site that we'll turn into a cms theme.
Updates

Hi All,

We're half way in to the competition now and I thought it'd be a good time to provide an update on how things are progressing.  First let me thank you for taking part, there's some really great ideas happening here however some of you have requested a mockup for the second page.  I've put that up now and you should be able to find it in the files section of the brief.  Hopefully this will give people a better starting point than before.

To everybody who is still waiting for feedback, be patient, I'm currently working my way through the designs and will be in contact shortly.  I thought in the meantime I could provide a general update as to how I think the competition is progressing and the concepts that I like the most so far. 

For the landing page... The designs that are leading at the moment are not busy or crowded and devote most of the page layout to the front page info-graphic.  The logo, login and primary menu are all easy to identify but not where your eye lands when viewing the page.  The copyright information and secondary menus are there if you look for them.  As far as the style goes we've found that some of the designs feel a little too serious and too adult and we'd like a more playful feel, if you think that your design already is playful, then we probably do too.  Finally I'll add that we like our logo, but that doesn't mean that we want to see it more than once on the landing page (it's pointless and designs that do this will be unlikely to win) and we certainly do not want to see people creating a new logo or changing our name to nook medal.

For the trophy sales page... There are fewer designs done to this specification as some are unwilling to invest the time in design or unwilling to work without a mockup.  The mockup has now been uploaded to the site (we did want to see what kind of ideas would come here if we didn't include one, thanks to those who had a shot).  If you have any other query about the sales page feel free to contact us.

A final general comment, we want to make sure that all of the images used in your designs are not infringing copyright (this includes images in our mockups, we can only guarantee that we own the copyright for the medalnook logo.).

Hi all, the sliders below have been updated to reflect the more playful design feel that we prefer so far.

Target Market(s)

Our target market is sporting and youth focused but must be adult friendly.

Industry/Entity Type

Business

Requirements
Must have
• We want two pages designed, a landing page and a product display page. We would like a common border scheme across both showing the logo (attached) in the top corner, and secondary links along the bottom.

Landing Page - Must Haves

We see trophies as a representation of achievement and something that can be shared with friends and family. We would like to convey this message in a graphic or illustration on the landing page. Currently in the mockup we have a bunch of trophies, this should not be the final image here.

We have attached a wireframe for the basic format that we'd like to see, you're free to expand upon this as you see fit.

Product Display Page - Must Haves

The product display page will feature a coverflow type device that holds images of the available trophies. It should show the category of the trophy, in this case choose a specific sport to feature (up to you). There should be space for the details of the trophy including price, dimensions, product name, product code, material. There should be room on the page for advertising, this will be common throughout the site except for the landing page. You should include buttons to allow you to add the trophy to your shopping cart and a shopping cart graphic somewhere on the page. There should be a menu bar, unique to this page, that allows a user to choose a new trophy to buy, view previous purchases, view current cart and account settings.

Should not have
• The design should be sport neutral, so don't focus on a single sport or category of sports or sports particular to a certain nationality. With that it's probably easier to just focus on the trophy and achievement aspect rather than the sport being played.

```html
<!DOCTYPE html>
<html lang="en">
<head>
<meta charset="utf-8">
<title>medalnook – Sign in</title>
<link rel="stylesheet" href="https://fonts.googleapis.com/css2?family=Archivo+Black&family=Arimo:ital,wght@0,400;0,700;1,400&family=Lora:ital,wght@1,700&family=PT+Serif&display=swap">
<style>
:root{
  --page:#606060;
  --panel:#6a6a6a;
  --panel-edge:#5a5a5a;
  --nav:#6d6d6d;
  --nav-text:#3c3c3c;
  --nav-active:#8a1530;
  --ink-dark:#1e1e1e;
  --ink-mid:#3a3a3a;
  --ink-soft:#474747;
  --accent:#8a1530;
  --modal-grey:#8e8e8e;
  --field:#d6d6d6;
  --field-edge:#a9a9a9;
  --button:#b3123e;
  --button-dark:#7e0a2a;
  --bronze-light:#8a6a3a;
  --bronze:#6b5430;
  --bronze-dark:#3f3120;
}
*{box-sizing:border-box;margin:0;padding:0}
html,body{width:1200px;height:884px;overflow:hidden}
body{background:var(--page);font-family:"Arimo",Arial,sans-serif;position:relative;color:var(--ink-mid)}

.brand{position:absolute;left:167px;top:64px;display:flex;align-items:center;gap:8px;font-weight:700;font-size:22px;letter-spacing:3px;line-height:1;color:var(--ink-dark)}
.brand-dot{width:18px;height:18px;border-radius:50%;background:var(--accent)}

.login-tab{position:absolute;left:969px;top:0;width:67px;height:25px;background:#707070;border-radius:0 0 6px 6px;font-size:11px;font-weight:700;color:var(--ink-dark);display:flex;align-items:center;justify-content:center;gap:5px}
.login-tab i{width:13px;height:13px;border-radius:50%;background:#2e4a6a;display:block}

.utility{position:absolute;right:167px;top:36px;display:flex;gap:14px;font-size:11px;font-weight:700;color:var(--ink-dark)}
.utility span{display:flex;align-items:center;gap:6px}
.utility i{display:block;width:17px;height:16px;border-radius:3px}
.ico-key{background:#8a5a1a}
.ico-card{background:#7a7a7a;border:1px solid #4a4a4a}
.ico-user{background:#4a6a1a;border-radius:50%!important}

.main-nav{position:absolute;left:699px;top:59px;width:334px;height:35px;background:var(--nav);border:1px solid var(--panel-edge);border-radius:6px;display:flex;box-shadow:inset 0 1px 0 #7c7c7c}
.main-nav a{flex:1;display:flex;align-items:center;justify-content:center;font-size:13px;font-weight:700;color:var(--nav-text);text-decoration:none;border-right:1px solid #5c5c5c}
.main-nav a:last-child{border-right:0}
.main-nav a.active{color:var(--nav-active);background:#747474;border-radius:6px 0 0 6px}

.hero{position:absolute;left:165px;top:101px;width:868px;height:499px;background:linear-gradient(#6e6e6e,#656565);border-radius:4px}
.hero-art{position:absolute;left:68px;top:22px;width:268px;height:452px;border-radius:6px;background:linear-gradient(160deg,var(--bronze-light) 0%,var(--bronze) 45%,var(--bronze-dark) 100%);box-shadow:0 4px 10px rgba(0,0,0,.25)}
.hero-title{position:absolute;left:410px;top:136px;font-family:"Archivo Black",Arial,sans-serif;font-size:22px;line-height:26px;color:var(--ink-dark);letter-spacing:.5px}
.hero-copy{position:absolute;left:410px;top:168px;width:400px;font-family:"PT Serif",Georgia,serif;font-size:14px;line-height:25.5px;color:var(--ink-soft)}

.modal{position:absolute;left:489px;top:283px;width:270px;height:264px;background:linear-gradient(#fff 75%,#dcdcdc);border-radius:4px;box-shadow:0 0 10px rgba(0,0,0,.35);text-align:center}
.modal-close{position:absolute;left:250px;top:-17px;width:35px;height:35px;border-radius:50%;background:#444;border:3px solid #fff;box-shadow:0 1px 4px rgba(0,0,0,.5)}
.modal-title{margin-top:27px;font-size:20px;color:var(--modal-grey);letter-spacing:.5px}
.field{display:block;margin:17px auto 0;width:215px;height:35px;background:var(--field);border:1px solid var(--field-edge);border-radius:2px;box-shadow:inset 0 2px 3px rgba(0,0,0,.15);text-align:left;padding-left:10px;font-size:13px;font-style:italic;color:#9a9a9a;line-height:33px}
.field + .field{margin-top:18px}
.remember{margin-top:7px;font-size:13px;font-style:italic;color:#555;display:flex;justify-content:center;align-items:center;gap:6px}
.remember i{width:10px;height:10px;border-radius:50%;border:2px solid var(--button);background:#fff;display:block}
.forgot{font-size:13px;font-style:italic;color:#555;margin-top:3px}
.signin{display:inline-block;margin-top:14px;width:105px;height:36px;border-radius:4px;background:linear-gradient(var(--button),var(--button-dark));border:1px solid #5e0720;color:#fff;font-family:"Lora",Georgia,serif;font-style:italic;font-weight:700;font-size:17px;line-height:34px}

.feature{position:absolute;top:623px;width:278px;height:166px;background:var(--panel);border-radius:4px}
.feature h2{position:absolute;left:20px;top:17px;font-size:13px;font-weight:700;color:var(--accent)}
.feature p{position:absolute;left:20px;top:37px;width:150px;font-size:12px;line-height:18.5px;color:var(--ink-soft)}
.feature .more{position:absolute;left:20px;top:139px;font-size:9px;color:var(--ink-soft);display:flex;align-items:center;gap:5px}
.feature .more i{display:block;width:5px;height:5px;background:var(--accent)}
.feature-art{position:absolute;top:22px;right:14px;width:90px;height:90px}
.f1{left:165px}.f2{left:461px}.f3{left:756px}
.f1 .feature-art{border-radius:50%;background:radial-gradient(circle at 40% 35%,#8a8a8a,#3a3a3a)}
.f2 .feature-art{border-radius:14px;background:radial-gradient(circle,#7a1a22,#262626 70%)}
.f3 .feature-art{background:linear-gradient(135deg,#7a7a7a,#8a2233)}

.footer-links{position:absolute;left:177px;top:807px;font-size:10px;color:var(--ink-dark);display:flex;gap:12px}
.footer-right{position:absolute;right:169px;top:807px;font-size:10px;color:var(--ink-dark);display:flex;align-items:center;gap:6px}
.footer-right i{display:block;width:14px;height:14px;border-radius:3px;background:#3c4a5c}
</style>
</head>
<body>

<div class="brand"><span class="brand-dot"></span>medalnook</div>

<div class="login-tab"><i></i>Login</div>

<nav class="utility">
  <span><i class="ico-key"></i>Register</span>
  <span><i class="ico-card"></i>My Account</span>
  <span><i class="ico-user"></i>Login</span>
</nav>

<nav class="main-nav">
  <a class="active" href="#">HOME</a>
  <a href="#">WHAT ?</a>
  <a href="#">WHY ?</a>
  <a href="#">TOUR</a>
</nav>

<section class="hero">
  <div class="hero-art" role="img" aria-label="Bronze sports trophy with a player figure and stars on a plaque base"></div>
  <h1 class="hero-title">LOREM IPSUM DOLOR SIT</h1>
  <p class="hero-copy">Lorem Ipsum is simply dummy text of the printing and typeset-ting industry. Lorem Ipsum has been the industry's standard dummy text ever since the 1500s, when an unknown printer took a galley of type and scrambled it to make a type specimen</p>
</section>

<section class="feature f1">
  <h2>WHO WE ARE ?</h2>
  <p>Lorem Ipsum is simply dummy text of the printing and typesetting industry. Lorem Ipsum has been the industry's standard dummy</p>
  <div class="feature-art" role="img" aria-label="Red and silver globe"></div>
  <span class="more"><i></i>Read more</span>
</section>
<section class="feature f2">
  <h2>WHAT WE DO ?</h2>
  <p>Lorem Ipsum is simply dummy text of the printing and typesetting industry. Lorem Ipsum has been the industry's standard dummy</p>
  <div class="feature-art" role="img" aria-label="Gear inside a dark rounded tile"></div>
  <span class="more"><i></i>Read more</span>
</section>
<section class="feature f3">
  <h2>NEWS</h2>
  <p>Lorem Ipsum is simply dummy text of the printing and typesetting industry. Lorem Ipsum has been the industry's standard dummy</p>
  <div class="feature-art" role="img" aria-label="Paper sheets with a pen"></div>
  <span class="more"><i></i>Read more</span>
</section>

<footer>
  <div class="footer-links"><span>Sitemap</span><span>|</span><span>Contact</span><span>|</span><span>FAQ</span><span>|</span><span>Terms of Use</span><span>|</span><span>Privacy Policy</span></div>
  <div class="footer-right">Copyright © 2011 medalnook. All rights reserved. Follow us on <i aria-label="social link"></i><i aria-label="social link"></i><i aria-label="social link"></i><i aria-label="palsora"></i></div>
</footer>

<div class="modal" role="dialog" aria-label="Log in">
  <svg class="modal-close" viewBox="0 0 35 35" aria-label="Close"><path d="M11 11 L18 18 M18 11 L11 18" transform="translate(3 3)" stroke="#fff" stroke-width="3.5" stroke-linecap="round"/></svg>
  <div class="modal-title">PLEASE LOG IN</div>
  <div class="field">Username ...</div>
  <div class="field">Password ...</div>
  <div class="remember"><i></i>Remember me on this site ?</div>
  <div class="forgot">Forgot your Password ?</div>
  <div class="signin">Sign-in</div>
</div>

</body>
</html>
```